Lunavel Aromatherapy Sleep Mask

We need package design for a new product we're introducing that allows for the integration of a variety of aromatherapy blends into a sleep mask. The blends are applied to scent wafers that are embedded inside the mask. The packaging should allow for incorporation of the mask, a .75ml vial of aromatherapy (2-⅛" tall and ⅞" in diameter), a small pipette(2-¼" in length) and five scent wafers (each ¾" in diameter) -- see attached pics. I'd also like to find a way to incorporate a small brochure inside the packaging to explain how to use the product and its benefits.

Target Market(s)

Target is cross gender. The majority of these masks will be used to enhance sleep and insomnia knows no gender preference. Demographic skew is likely college educated, upscale with HHI of $100K+.

Industry/Entity Type

Product

Font styles to use
Serif
Sans Serif

Requirements
Must have
• The ability to incorporate all components: mask, aromatherapy vial, pipette and scent wafers. While I'm happy to review all designs, I need to make sure that the actual production remains affordable so please keep that in mind. Color palette must work with the logo (attached) and be soothing in nature.
Nice to have
• I'd like to see a box option where all components can be securely packaged. I also think it would be nice if the customer can see the actual mask as they will come in a variety of fabrics. Am open to any other suggestions you all have.

```html
<!DOCTYPE html>
<html lang="en">
<head>
<meta charset="utf-8">
<title>Lunavel Aromatherapy Sleep Mask – Package</title>
<link rel="stylesheet" href="https://fonts.googleapis.com/css2?family=Comfortaa:wght@300;400&display=swap">
<style>
  :root {
    --canvas: #ffffff;
    --panel-border: #c9c9c9;
    --mint-light: #d9f0ea;
    --mint: #bfe5db;
    --brand-teal: #8fd0c3;
    --title-teal: #7fb3a8;
    --tray: #d5d6d7;
    --tray-floor: #e2e3e4;
    --tray-edge: #f4f4f4;
    --vial-brown: #7a3d17;
    --pipette: #d2ab93;
    --wafer: #e8c89a;
    --fabric-blue: #1f8fc4;
    --fabric-violet: #5a3a8e;
    --fabric-olive: #b8c25a;
    --fabric-teal: #1fa3a0;
  }
  * { box-sizing: border-box; margin: 0; padding: 0; }
  html, body {
    width: 1200px; height: 1160px; overflow: hidden;
    background: var(--canvas);
    font-family: "Comfortaa", sans-serif;
  }
  .package { position: relative; width: 1200px; height: 1160px; }

  /* Lid */
  .lid {
    position: absolute; left: 92px; top: 33px;
    width: 1016px; height: 534px;
    border: 2px solid var(--panel-border);
    background: var(--canvas);
    overflow: hidden;
  }
  .lid__wave { position: absolute; inset: 0; width: 100%; height: 100%; }
  .brand {
    position: absolute; left: 330px; top: 108px;
    font-weight: 300; font-size: 96px; line-height: 1;
    letter-spacing: 2px; color: var(--brand-teal);
  }
  .brand__dot {
    position: absolute; left: 240px; top: 132px;
    width: 56px; height: 56px; border-radius: 50%;
    background: var(--mint);
  }
  .lid__window {
    position: absolute; left: 383px; top: 206px;
    width: 467px; height: 166px;
    border-radius: 48px;
    border: 4px solid var(--canvas);
    background: linear-gradient(90deg, var(--fabric-blue), var(--fabric-violet) 30%, var(--fabric-olive) 50%, var(--fabric-teal) 75%, var(--fabric-violet));
  }
  .lid__face {
    position: absolute; left: 552px; top: 386px;
    width: 146px; height: 136px; border-radius: 50%;
    background: radial-gradient(ellipse at center, var(--mint-light) 0%, var(--mint) 80%);
  }
  .lid__title {
    position: absolute; left: 105px; top: 440px;
    font-weight: 300; font-size: 74px; line-height: 1;
    color: var(--title-teal);
  }

  /* Tray */
  .tray {
    position: absolute; left: 92px; top: 587px;
    width: 1016px; height: 488px;
    border: 2px solid var(--panel-border);
    background: var(--canvas);
  }
  .tray__well {
    position: absolute; left: 18px; top: 18px; right: 18px; bottom: 18px;
    background: var(--tray-floor);
    border: 10px solid var(--tray);
    border-right-color: var(--tray-edge);
    border-bottom-color: var(--tray-edge);
    overflow: hidden;
  }
  .vial {
    position: absolute; left: 33px; top: 13px; width: 92px; height: 128px;
    border-radius: 8px;
    background: linear-gradient(180deg, #1c1c1c 0 28%, var(--vial-brown) 28%);
  }
  .pipette {
    position: absolute; left: 428px; top: 58px; width: 288px; height: 33px;
    border-radius: 8px; background: var(--pipette);
  }
  .wafers {
    position: absolute; left: 786px; top: 50px; width: 112px; height: 80px;
    border-radius: 50%; background: var(--wafer);
  }
  .tray__mask {
    position: absolute; left: 28px; top: 141px; width: 917px; height: 250px;
    border-radius: 60px;
    background: linear-gradient(90deg, var(--fabric-blue), var(--fabric-violet) 25%, var(--fabric-olive) 45%, var(--fabric-teal) 70%, var(--fabric-violet));
  }
</style>
</head>
<body>
<main class="package">

  <section class="lid" aria-label="Box lid">
    <svg class="lid__wave" viewBox="0 0 1016 534" preserveAspectRatio="none" aria-hidden="true">
      <path d="M0,250 C240,280 330,350 470,345 C560,342 640,330 760,300 C860,275 950,250 1016,245 L1016,534 L0,534Z" fill="var(--mint-light)"/>
      <path d="M0,300 C200,330 330,385 450,362 C520,348 545,330 585,343 C660,368 790,330 1016,282 L1016,534 L0,534Z" fill="var(--mint)" stroke="#ffffff" stroke-width="8"/>
    </svg>

    <span class="brand__dot" aria-hidden="true"></span>
    <h1 class="brand">lunavel</h1>

    <div class="lid__window" role="img" aria-label="Window showing the printed fabric of the sleep mask"></div>
    <div class="lid__face" role="img" aria-label="Line illustration of a sleeping person"></div>
    <h2 class="lid__title">sleep mask</h2>
  </section>

  <section class="tray" aria-label="Box interior">
    <div class="tray__well">
      <div class="vial" role="img" aria-label="Amber aromatherapy vial, 75ml"></div>
      <div class="pipette" role="img" aria-label="Pipette"></div>
      <div class="wafers" role="img" aria-label="Stack of scent wafers"></div>
      <div class="tray__mask" role="img" aria-label="Printed fabric sleep mask with elastic strap"></div>
    </div>
  </section>

</main>
</body>
</html>
```